Management Consulting needing a cool business card for client acquisition and networking

We are looking for a business card that is progressive and fresh that conveys innovation, forward thinking, and confidence. The business card is for a company based in Charlotte NC called, 'MERIDOX CONSULTING GROUP LLC'. The company primarily works with banks, insurance, and brokerages to implement innovative solutions to help them streamline their operations, to more effectively manage risks, and to improve their customer relationships.

Target Market(s)

Typically meet with Chief Financial Officers, Chief Information Officers, Chief Operations Officer, Business Unit Leader. The target market are generally 40-55 years, male, white, master level education plus.

Industry/Entity Type

Progressive

Font styles to use
Serif
Other font styles liked:
• Calibri

Requirements
Should not have
• Designs that look too much like law firms or accounting companies. Too conservative

```html
<!DOCTYPE html>
<html lang="en">
<head>
<meta charset="utf-8">
<title>Meridox Consulting Group – Business Card</title>
<link rel="stylesheet" href="https://fonts.googleapis.com/css2?family=Bree+Serif&family=Kreon:wght@300;400&family=Open+Sans:wght@700&display=swap">
<style>
  :root {
    --canvas: #ffffff;
    --frame: #e9f1e2;
    --frame-edge: #9fc28a;
    --green-deep: #1f5a1f;
    --green-mid: #2f8a2c;
    --green-bright: #5cbd2e;
    --ink: #2c5a2a;
    --white: #ffffff;
  }
  * { margin: 0; padding: 0; box-sizing: border-box; }
  html, body { width: 1200px; height: 1000px; overflow: hidden; background: var(--canvas); }
  .sheet { position: relative; width: 1200px; height: 1000px; }

  .card {
    position: absolute; left: 173px; width: 776px; height: 461px;
    background: var(--frame);
    border-right: 2px solid var(--frame-edge);
    border-bottom: 3px solid var(--frame-edge);
  }
  .card--front { top: 18px; }
  .card--back { top: 510px; }

  .card__field {
    position: absolute; left: 9px; top: 10px; width: 758px; height: 438px;
    background:
      radial-gradient(ellipse at 40% 80%, rgba(92,189,46,.55), transparent 60%),
      linear-gradient(160deg, var(--green-mid) 0%, var(--green-deep) 35%, var(--green-mid) 65%, var(--green-bright) 100%);
    overflow: hidden;
  }

  .punch { position: absolute; left: 12px; top: 7px; width: 32px; height: 32px; border-radius: 50%; background: var(--white); }

  .brand-word {
    position: absolute; left: 24px; width: 170px; text-align: center;
    font-family: "Kreon", serif; font-weight: 400; font-size: 30px; color: var(--white);
    letter-spacing: 1px;
  }
  .card--front .brand-word { top: 98px; }
  .card--back .brand-word { top: 98px; }

  .rule { position: absolute; height: 8px; border-radius: 4px; background: linear-gradient(#ffffff, #dfe9d8); box-shadow: 0 1px 2px rgba(0,0,0,.3); }
  .card--front .rule { left: 208px; top: 73px; width: 483px; }
  .card--back .rule { left: 153px; top: 158px; width: 605px; }

  .company {
    position: absolute; left: 200px; width: 500px; text-align: center;
    font-family: "Bree Serif", serif; font-size: 34px; line-height: 1; color: var(--white);
    text-shadow: 2px 2px 0 rgba(0,0,0,.35);
  }
  .company--line1 { top: 32px; }
  .company--line2 { top: 90px; }

  .info-panel {
    position: absolute; left: 153px; top: 158px; width: 596px; height: 250px;
    background: linear-gradient(115deg, #8fcb6f 0%, #f1f7ec 42%, #a9d98e 70%, #58b53a 100%);
    box-shadow: 6px 8px 12px rgba(0,0,0,.45);
    font-family: "Kreon", serif; color: var(--ink);
  }
  .name-plate {
    position: absolute; left: 54px; top: 20px; width: 490px; height: 79px;
    background: #fafafa; border-radius: 9px; text-align: center;
  }
  .person-name { display: inline-block; margin-top: 6px; font-size: 30px; font-weight: 300; border-bottom: 1px solid var(--ink); line-height: 1.05; }
  .person-title { font-size: 22px; font-weight: 300; margin-top: 2px; }
  .address { position: absolute; left: 0; width: 100%; text-align: center; font-weight: 300; }
  .address--street { top: 118px; font-size: 23px; }
  .address--city { top: 157px; font-size: 17px; }
  .phone { position: absolute; top: 214px; font-size: 19px; font-weight: 300; }
  .phone--office { left: 57px; }
  .phone--cell { right: 55px; top: 211px; }

  .initials {
    position: absolute; left: 0; top: 196px; width: 100%; text-align: center; padding-left: 150px;
    font-family: "Open Sans", sans-serif; font-weight: 700; font-size: 58px; color: var(--white); letter-spacing: 2px;
  }
  .website {
    position: absolute; left: 0; top: 400px; width: 100%; text-align: center; padding-left: 30px;
    font-family: "Bree Serif", serif; font-size: 30px; color: var(--white);
    text-shadow: 2px 2px 0 rgba(0,0,0,.4);
  }
</style>
</head>
<body>
<main class="sheet">
  <section class="card card--front">
    <div class="card__field" role="img" aria-label="Green low-poly faceted triangle texture">
      <span class="punch"></span>
      <span class="brand-word">MERIDOX</span>
      <h1 class="company company--line1">MERIDOX CONSULTING</h1>
      <div class="rule"></div>
      <p class="company company--line2">GROUP LLC</p>
      <div class="info-panel">
        <div class="name-plate">
          <span class="person-name">DANIEL R. VOSS</span>
          <p class="person-title">CHIEF SOLUTIONS ARCHITECT</p>
        </div>
        <p class="address address--street">1825 LAKESIDE AVE., SUITE 300</p>
        <p class="address address--city">CHARLOTTE, NC 28207</p>
        <p class="phone phone--office">O : 704.555.0142</p>
        <p class="phone phone--cell">C : 704.555.0187</p>
      </div>
    </div>
  </section>

  <section class="card card--back">
    <div class="card__field" role="img" aria-label="Green low-poly faceted triangle texture">
      <span class="punch"></span>
      <span class="brand-word">MERIDOX</span>
      <div class="rule"></div>
      <p class="initials">D.A.N.I.E.L</p>
      <p class="website">WWW.MERIDOXCONSULTING.COM</p>
    </div>
  </section>
</main>
</body>
</html>
```